Property investor needs a business card with logo

I need a business card for a UK based business called 'Bright Gate Homes'. I buy houses quickly that is either hard to sell or people have been having trouble to sell. I then create the opportunity for people to buy houses that normally can't. This could be because they have little or no deposit saved up or they don't qualify for a mortgage. The design is to be bright so that it stands out but non threatening and basic. Yellow for the bass colour. The logo to be very simple and represent a house. It could include words like "cant sell? I'll buy it!!" or "Need a quick sale? Let me help" or something as simple as "I buy houses!!" The final design should communicate that I am not some big corporate person that is better that them, but someone that is just a person trying to help them with their situation. with a picture of me with the background removed.
Target Market(s)
Normal everyday people
Industry/Entity Type
Business
Contact Information for Business Card
Gareth Pellingham
07845619027
brightgatehomes@mailbox.example
Font styles to use
Other font styles liked:
- something that looks hand written
Look and feel
Each slider illustrates characteristics of the customer's brand and the style your logo design should communicate.

```html
<!DOCTYPE html>
<html lang="en">
<head>
<meta charset="utf-8">
<title>Bright Gate Homes – Business Card</title>
<link href="https://fonts.googleapis.com/css2?family=Mali:wght@600&display=swap" rel="stylesheet">
<style>
  :root {
    --card-yellow: #f8ea26;
    --card-red: #ea3c49;
    --portrait-dark: #2a2d33;
    --portrait-skin: #c99580;
    --page-bg: #e9e6e1;
    --card-font: "Mali", "Comic Neue", cursive;
  }
  * { box-sizing: border-box; margin: 0; padding: 0; }
  html, body { width: 1200px; height: 1000px; overflow: hidden; }
  body { background: var(--page-bg); position: relative; font-family: var(--card-font); font-weight: 600; }

  .card {
    position: absolute;
    background: var(--card-yellow);
    overflow: hidden;
    box-shadow: 0 4px 14px rgba(0,0,0,.18);
  }
  .card-back  { left: 40px;  top: 90px;  width: 725px; height: 477px; }
  .card-front { left: 436px; top: 435px; width: 724px; height: 475px; }

  .wave { position: absolute; inset: 0; width: 100%; height: 100%; }
  .wave path { fill: var(--card-red); }

  .portrait {
    position: absolute; left: 0; top: 45px; width: 385px; height: 330px;
    background: linear-gradient(180deg, var(--portrait-skin) 0%, var(--portrait-skin) 50%, var(--portrait-dark) 80%);
    border-radius: 50% 50% 0 0 / 45% 45% 0 0;
  }

  .brand-mark {
    position: absolute;
    width: 110px; height: 110px;
    background: var(--card-red);
  }
  .card-back .brand-mark  { left: 495px; top: 62px; }
  .card-front .brand-mark { left: 462px; top: 82px; width: 120px; height: 120px; }

  .brand-name {
    position: absolute;
    color: var(--card-red);
    font-size: 32px;
    white-space: nowrap;
  }
  .card-back .brand-name  { left: 393px; top: 188px; }
  .card-front .brand-name { left: 325px; top: 228px; font-size: 34px; }

  .back-tagline {
    position: absolute; left: 225px; top: 372px;
    color: var(--card-yellow); font-size: 58px; letter-spacing: 4px;
    white-space: nowrap;
    transform: rotate(-6deg); transform-origin: left bottom;
  }

  .speech-bubble { position: absolute; left: 30px; top: 32px; width: 320px; height: 230px; }
  .speech-bubble path { fill: var(--card-red); }
  .bubble-text {
    position: absolute; left: 68px; top: 66px;
    color: var(--card-yellow); line-height: 1; letter-spacing: 3px;
  }
  .bubble-text .line-big { display: block; font-size: 58px; }
  .bubble-text .line-small { display: block; font-size: 40px; margin: 6px 0 0 10px; }

  .contact { position: absolute; left: 34px; top: 320px; color: var(--card-yellow); }
  .contact-name { font-size: 30px; letter-spacing: 2px; margin-bottom: 12px; }
  .contact-row { display: flex; align-items: center; gap: 12px; font-size: 24px; letter-spacing: 2px; margin-bottom: 8px; white-space: nowrap; }
  .contact-icon { width: 30px; height: 30px; flex: none; }
</style>
</head>
<body>

<section class="card card-back">
  <div class="portrait" role="img" aria-label="Cut-out photo of the business owner in a dark fleece"></div>
  <svg class="wave" viewBox="0 0 725 477" preserveAspectRatio="none" aria-hidden="true">
    <path d="M0,365 C150,392 300,330 420,300 C540,270 640,262 725,268 L725,477 L0,477 Z"/>
  </svg>
  <div class="brand-mark" aria-hidden="true"></div>
  <div class="brand-name">Bright Gate Homes</div>
  <div class="back-tagline">I buy houses!!</div>
</section>

<section class="card card-front">
  <svg class="wave" viewBox="0 0 724 475" preserveAspectRatio="none" aria-hidden="true">
    <path d="M0,285 C120,262 230,270 360,300 C500,332 620,375 724,375 L724,475 L0,475 Z"/>
  </svg>

  <svg class="speech-bubble" viewBox="0 0 320 230" aria-hidden="true">
    <path d="M60,30 C80,0 140,0 160,20 C185,0 250,5 260,40 C300,40 320,80 300,110
             C325,140 305,190 260,185 C240,210 200,205 185,195 L180,228 L160,195
             C120,210 70,205 60,180 C20,185 0,150 15,120 C-5,90 10,45 60,30 Z"/>
  </svg>
  <div class="bubble-text">
    <span class="line-big">I BUY</span>
    <span class="line-small">HOUSES!!</span>
  </div>

  <div class="brand-mark" aria-hidden="true"></div>
  <div class="brand-name">Bright Gate Homes</div>

  <div class="contact">
    <div class="contact-name">Gareth Pellingham</div>
    <div class="contact-row">
      <svg class="contact-icon" viewBox="0 0 30 30" aria-hidden="true">
        <circle cx="15" cy="15" r="15" fill="var(--card-yellow)"/>
        <rect x="10" y="6" width="10" height="18" rx="2" fill="none" stroke="var(--card-red)" stroke-width="2.5"/>
        <circle cx="15" cy="20" r="1.3" fill="var(--card-red)"/>
      </svg>
      <span>07845619027</span>
    </div>
    <div class="contact-row">
      <svg class="contact-icon" viewBox="0 0 30 30" aria-hidden="true">
        <circle cx="15" cy="15" r="15" fill="var(--card-yellow)"/>
        <rect x="6.5" y="9.5" width="17" height="11" fill="none" stroke="var(--card-red)" stroke-width="2"/>
        <path d="M6.5,9.5 L15,16 L23.5,9.5" fill="none" stroke="var(--card-red)" stroke-width="2"/>
      </svg>
      <span>brightgatehomes@mailbox.example</span>
    </div>
  </div>
</section>

</body>
</html>
```